Business card design for global fintech startup

Veltrix is a modern payments platform for the global insurance industry, serving international health, life, and travel insurers, MGAs, brokers, and partners.

We need a professional, premium business card for use at insurance conferences and executive meetings. The goal is to create a card that feels trustworthy, modern, and high-quality, while still being distinctive and memorable in a stack of business cards.

Target audience:
Senior insurance executives (VP, C-suite).

Design goals:
Clear, professional, and credible
Modern but not trendy
Premium and well-structured
Easy to read and practical for networking

Brand direction:
Brand-first (company over individual)
Follow existing brand guidelines where possible
Clean layout, strong hierarchy, excellent readability

Must include:
Name
Title
Company name (Veltrix)
Logo
Email
Phone/Whatsapp
Website (www.withveltrix.example)
Tagline - Clarity In Every Transfer

Materials & finish:
Open to designer recommendations for premium look and feel.

Please avoid:
Flashy or trendy startup styles
Generic insurance icons or clichés
Cluttered layouts or hard-to-read text

Deliverables:
Front and back business card, print-ready files.

Target Market(s)

Global Insurance executives

Industry/Entity Type

Fintech, Insurtech, Insurance, Financial Services

Contact Information for Business Card

Name Title Company name (Veltrix) Logo Email Phone/Whatsapp Website (www.withveltrix.example) Tagline - Clarity In Every Transfer

Font styles to use
Other font styles liked:
• See brand guidelines

Requirements
Nice to have
• something that stands out/makes us more memorable while still remaining professional
Should not have
• Please avoid: Flashy or trendy startup styles Generic insurance icons or clichés Cluttered layouts or hard-to-read text

```html
<!DOCTYPE html>
<html lang="en">
<head>
<meta charset="utf-8">
<title>Veltrix Business Card – Front and Back</title>
<link rel="stylesheet" href="https://fonts.googleapis.com/css2?family=Ubuntu:wght@400;500;700&display=swap">
<style>
  :root {
    --canvas: #d2d1d2;
    --card-dark: #231f20;
    --card-light: #ffffff;
    --ink: #231f20;
    --muted: #9a9a9a;
    --link: #2f7fcf;
    --orange: #f47b20;
    --yellow: #f9c55c;
    --purple: #5b4a9e;
    --blue: #3a86cc;
    --cyan: #41c4ee;
  }
  * { margin: 0; padding: 0; box-sizing: border-box; }
  html, body {
    width: 892px;
    height: 1200px;
    overflow: hidden;
    background: var(--canvas);
    font-family: "Ubuntu", sans-serif;
  }
  .sheet {
    position: relative;
    width: 892px;
    height: 1200px;
  }
  .card {
    position: absolute;
    width: 424px;
    height: 242px;
    overflow: hidden;
  }

  /* Back: brand side */
  .card--back {
    left: 124px;
    top: 352px;
    background: var(--card-dark);
    color: #fff;
  }
  .card--back .wordmark {
    position: absolute;
    left: 0;
    right: 0;
    top: 98px;
    text-align: center;
    font-size: 38px;
    font-weight: 500;
    letter-spacing: 4px;
    line-height: 1;
  }
  .card--back .tagline {
    position: absolute;
    left: 0;
    right: 0;
    top: 204px;
    text-align: center;
    font-size: 11.5px;
    font-weight: 400;
    letter-spacing: 0.2px;
    line-height: 1;
  }

  /* Front: contact side */
  .card--front {
    left: 339px;
    top: 609px;
    background: var(--card-light);
    color: var(--ink);
  }
  .card--front .wordmark {
    position: absolute;
    left: 46px;
    top: 40px;
    font-size: 22px;
    font-weight: 500;
    letter-spacing: 2.4px;
    line-height: 1;
  }
  .person {
    position: absolute;
    left: 46px;
    top: 106px;
  }
  .person__name {
    font-size: 18.5px;
    font-weight: 700;
    line-height: 1.1;
  }
  .person__title {
    margin-top: 3px;
    font-size: 10.5px;
    color: var(--muted);
  }
  .contact {
    position: absolute;
    left: 46px;
    top: 162px;
    list-style: none;
    font-size: 10.5px;
    color: var(--muted);
  }
  .contact li {
    display: flex;
    align-items: center;
    gap: 5px;
    height: 15px;
  }
  .contact svg { width: 8px; height: 8px; }
  .website {
    position: absolute;
    left: 46px;
    top: 202px;
    font-size: 12.5px;
    color: var(--link);
  }
  .accent-band {
    position: absolute;
    right: 0;
    top: 0;
    width: 96px;
    height: 100%;
    background: linear-gradient(180deg, var(--purple) 0%, var(--blue) 35%, var(--cyan) 55%, var(--orange) 78%, var(--yellow) 100%);
  }
</style>
</head>
<body>
  <main class="sheet">
    <section class="card card--back" aria-label="Business card back">
      <div class="wordmark">VELTRIX</div>
      <div class="tagline">CLARITY IN EVERY TRANSFER</div>
    </section>

    <section class="card card--front" aria-label="Business card front">
      <div class="wordmark">VELTRIX</div>

      <div class="person">
        <div class="person__name">Elena Marsh - Whitford</div>
        <div class="person__title">President</div>
      </div>

      <ul class="contact">
        <li>
          <svg viewBox="0 0 10 10" aria-hidden="true"><path d="M2 1 L4 1 L4.6 3 L3.4 3.8 Q4.4 5.8 6.2 6.6 L7 5.4 L9 6 L9 8 Q5 9 1 4 Q1 2 2 1Z" fill="none" stroke="currentColor" stroke-width="0.9"/></svg>
          <span>355-010-0199</span>
        </li>
        <li>
          <svg viewBox="0 0 10 10" aria-hidden="true"><rect x="1" y="2" width="8" height="6" fill="none" stroke="currentColor" stroke-width="0.9"/><path d="M1 2 L5 5.5 L9 2" fill="none" stroke="currentColor" stroke-width="0.9"/></svg>
          <span>info@withveltrix.example</span>
        </li>
      </ul>

      <div class="website">www.withveltrix.example</div>

      <div class="accent-band"></div>
    </section>
  </main>
</body>
</html>
```